Sunvale Energy UK Flyer Design, for local domestic and commercial properties.

We are a renewable energy company called "SUNVALE ENERGY UK" we specialize in
Electrical and renewable energy project consultancy.
Solar panel installations
battery storage.
Electrical design and installation from Stage 3

Details can be found on our website: www.sunvaleenergyuk.co.uk
Am looking to have a flyer designed so we can have printed and delivered to all local areas.
We carry out free project surveys and offer full project transparency through out the clients journey.
attached is our logo of which i hope may help.

Target Market(s)

Domestic and commercial properties looking to dramatically reduce energy bills

Industry/Entity Type

Domestic, commercial, industrial, mixed used development and much more.

Font styles to use
Serif
Sans Serif
Decorative

Colors
FFC000
F8CF3A
FAE287
FDF2CF
FEFAEE
F0912C
F2A743
F7CA91
FBE8D2
FDF5EE
EE7325
F08F49
F5BC92
FAE3D3
FDF4ED

Requirements
Must have
• Highlight we offer free quotations and offer a fully transparent project processes from design, installation Plus leading health and safety process no matter what size project.
Nice to have
• Pictures of solar panel systems, i have attached a few pictures which you may wish to edit or take snippets etc.

```html
<!DOCTYPE html>
<html lang="en">
<head>
<meta charset="utf-8">
<title>Sunvale Energy UK – Flyer</title>
<link href="https://fonts.googleapis.com/css2?family=Roboto+Condensed:wght@400;500;700&family=Nunito:wght@600;800&display=swap" rel="stylesheet">
<style>
  :root{
    --navy:#2b344a;
    --navy-deep:#252d41;
    --orange:#f0912c;
    --orange-deep:#ee7325;
    --orange-soft:#f2a743;
    --white:#ffffff;
    --sky:#8fb2d6;
    --panel:#3d5478;
  }
  *{margin:0;padding:0;box-sizing:border-box}
  html,body{width:984px;height:1200px;overflow:hidden;background:#eeeae4}
  .flyer{position:relative;width:984px;height:1200px;background:var(--navy);overflow:hidden;font-family:"Roboto Condensed",Arial,sans-serif;color:var(--white)}
  .shapes{position:absolute;inset:0}
  .hero-photo{position:absolute;left:283px;top:120px;width:701px;height:352px;
    background:linear-gradient(180deg,#7ea6cf 0%,#c9d9e8 35%,#9ab4cf 55%,#4d6a92 72%,#33476a 100%);
    -webkit-mask-image:linear-gradient(90deg,transparent 0%,#000 40%);
    mask-image:linear-gradient(90deg,transparent 0%,#000 40%)}
  .brand{position:absolute;top:40px;left:0;width:984px;display:flex;justify-content:center;align-items:center;gap:14px}
  .brand-dot{width:38px;height:38px;border-radius:50%;background:var(--orange)}
  .brand-name{font-family:"Roboto Condensed",Arial,sans-serif;font-weight:500;font-size:34px;letter-spacing:3px;color:var(--navy)}
  .headline{position:absolute;left:73px;top:190px;font-size:54px;font-weight:400;line-height:60px}
  .headline .accent{color:var(--orange)}
  .offer{position:absolute;left:79px;top:328px}
  .offer-title{font-size:25px;font-weight:700;color:var(--orange);margin-bottom:4px}
  .offer-list{list-style:none}
  .offer-list li{font-size:25px;font-weight:700;line-height:27px;display:flex;align-items:center;gap:8px}
  .offer-list li::before{content:"";width:16px;height:16px;border-radius:50%;background:var(--orange);box-shadow:0 0 0 3px rgba(240,145,44,.35)}
  .ribbon{position:absolute;height:32px;right:0;display:flex;align-items:center;gap:12px;padding-left:28px;
    font-size:24px;font-weight:700;text-transform:uppercase;
    background:linear-gradient(90deg,var(--orange-deep) 0%,var(--orange) 55%,rgba(240,145,44,.45) 100%);
    clip-path:polygon(0 0,100% 0,100% 100%,18px 100%)}
  .ribbon svg{width:16px;height:16px;flex:none}
  .photo{position:absolute}
  .photo-plant{left:24px;top:689px;width:276px;height:352px;background:linear-gradient(180deg,#e9e4dc,#b98a5f 60%,#8b6a4c)}
  .photo-roof{left:320px;top:689px;width:311px;height:356px;background:linear-gradient(180deg,#8fb0d8 0%,#a8c1df 25%,#1f2634 45%,#2a3244 70%,#9a5a43 100%)}
  .photo-array{left:651px;top:687px;width:311px;height:358px;background:linear-gradient(180deg,#c7d3e2 0%,#4f6b3d 25%,#1b2232 50%,#2e3a55 80%,#8a7d6a 100%)}
  .footer{position:absolute;left:0;top:1074px;width:984px;height:126px;background:var(--navy)}
  .cta{position:absolute;left:23px;top:1110px;font-size:42px;font-weight:400;letter-spacing:.5px;display:flex;align-items:center;gap:10px}
  .cta .accent{color:var(--orange);font-weight:700}
  .cta-arrow{width:0;height:0;border-top:13px solid transparent;border-bottom:13px solid transparent;border-left:10px solid #4a5470}
  .contact{position:absolute;left:412px;top:1108px;font-family:"Nunito",Arial,sans-serif}
  .contact-row{display:flex;align-items:center;gap:12px}
  .contact-row svg{width:20px;height:20px;flex:none}
  .contact-email{font-size:18px;font-weight:800}
  .contact-phone{font-size:29px;font-weight:600;line-height:34px}
  .web-tag{position:absolute;left:723px;top:1116px;width:261px;height:45px;background:var(--orange-deep);
    clip-path:polygon(22px 0,100% 0,100% 100%,0 100%);display:flex;align-items:center;gap:10px;padding-left:34px;
    font-family:"Nunito",Arial,sans-serif;font-weight:800;font-size:17px}
  .web-tag svg{width:14px;height:18px;flex:none}
</style>
</head>
<body>
<main class="flyer">
  <div class="hero-photo" role="img" aria-label="Photograph of rooftop solar panels under a bright cloudy sky"></div>

  <svg class="shapes" width="984" height="1200" viewBox="0 0 984 1200" aria-hidden="true">
    <polygon points="0,86 491,143 984,101 984,122 491,147 0,106" fill="var(--orange)"/>
    <polygon points="0,0 984,0 984,101 491,143 0,86" fill="var(--white)"/>
    <polygon points="0,620 330,690 330,981 0,981" fill="var(--orange)"/>
    <polygon points="640,900 984,843 984,981 640,981" fill="var(--orange-deep)"/>
    <rect x="0" y="981" width="984" height="93" fill="var(--orange-deep)"/>
  </svg>

  <header class="brand">
    <span class="brand-dot"></span>
    <span class="brand-name">SUNVALE ENERGY UK</span>
  </header>

  <h1 class="headline">Reduce Energy Bills<br><span class="accent">With Renewable Energy</span></h1>

  <section class="offer">
    <h2 class="offer-title">We Offer</h2>
    <ul class="offer-list">
      <li>Electrical and renewable project consultancy.</li>
      <li>Solar panel installations</li>
      <li>battery storage.</li>
    </ul>
  </section>

  <div class="ribbon" style="top:474px;left:454px">
    <svg viewBox="0 0 16 16"><path d="M2 8.5l4 4 8-9" fill="none" stroke="#fff" stroke-width="1.8"/></svg>Full project transparency</div>
  <div class="ribbon" style="top:517px;left:476px;padding-left:32px">
    <svg viewBox="0 0 16 16"><path d="M2 8.5l4 4 8-9" fill="none" stroke="#fff" stroke-width="1.8"/></svg>Installation</div>
  <div class="ribbon" style="top:561px;left:498px">
    <svg viewBox="0 0 16 16"><path d="M2 8.5l4 4 8-9" fill="none" stroke="#fff" stroke-width="1.8"/></svg>Health and safety process</div>
  <div class="ribbon" style="top:603px;left:521px;padding-left:32px">
    <svg viewBox="0 0 16 16"><path d="M2 8.5l4 4 8-9" fill="none" stroke="#fff" stroke-width="1.8"/></svg>Domestic and commercial</div>

  <div class="photo photo-plant" role="img" aria-label="Photograph of an inverter and battery storage installation on a plant room wall"></div>
  <div class="photo photo-roof" role="img" aria-label="Photograph of black solar panels on a tiled house roof with scaffolding"></div>
  <div class="photo photo-array" role="img" aria-label="Photograph of a large solar panel array on a flat roof with trees behind"></div>

  <footer class="footer"></footer>
  <div class="cta">GET A <span class="accent">FREE</span> QUOTE <span class="cta-arrow"></span></div>
  <div class="contact">
    <div class="contact-row contact-email">
      <svg viewBox="0 0 20 20"><rect x="2" y="4" width="16" height="12" fill="none" stroke="var(--orange)" stroke-width="1.8"/><path d="M2 4l8 7 8-7" fill="none" stroke="var(--orange)" stroke-width="1.8"/></svg>
      info@sunvaleenergyuk.co.uk</div>
    <div class="contact-row contact-phone">
      <svg viewBox="0 0 20 20"><rect x="5" y="1" width="10" height="18" rx="2" fill="none" stroke="var(--orange)" stroke-width="2"/><rect x="7" y="5" width="6" height="6" fill="var(--orange)"/></svg>
      0800 555 0142</div>
  </div>
  <div class="web-tag">
    <svg viewBox="0 0 14 18"><path d="M1 1l12 10h-6l3 6-2 1-3-6-4 4z" fill="var(--navy)"/></svg>
    sunvaleenergyuk.co.uk</div>
</main>
</body>
</html>
```